Redesign website bus travel company Lenz Tavan

We require a complete redesign of the website of Reisebüro Lenz Tavan, an established bus tour operator based in Graubünden (www.lenztavan-beispiel.ch). For years, the company has specialized in multi-day tours throughout Europe, as well as day trips such as shopping trips to Innsbruck or Como, music tours, and market visits, primarily for seniors, as well as car rentals for clubs and companies.

The new website requires a video header with overlay text, red as the primary corporate color, complemented by black and gray, and a highly simplified navigation with two main sections: "Our Trips" and "Bus Rental." The remaining sections must be accessible via the "Menu" menu item. The design should be user-friendly for all age groups and mobile-responsive.

The goal is a trustworthy, modern website that reflects personal service and many years of experience.
The new logo can be found in the files, as well as a few pictures.

Target Market(s)

Guests of bus tours (day and multi-day trips) and bus rentals (clubs, companies, etc.)

Industry/Entity Type

Busreisen und Busvermietung

Number of Pages Required

1 page

Requirements
Must have
• Red as primary color, video header, simple UX for target group seniors
Nice to have
• Photo galleries of destinations and the vehicle fleet

```html
<!DOCTYPE html>
<html lang="de">
<head>
<meta charset="utf-8">
<title>Lenz Tavan – Busreisen &amp; Busvermietung</title>
<link href="https://fonts.googleapis.com/css2?family=Lora:wght@500;600&family=Poppins:wght@400;500;600&display=swap" rel="stylesheet">
<style>
:root{
  --red:#c8191f;
  --red-dark:#a4121a;
  --ink:#1e1e1e;
  --grey:#6a6a6a;
  --line:#d9d9d9;
  --blush:#f8e5e6;
  --cream:#fdf6e6;
  --footer:#1c0306;
  --white:#fff;
}
*{box-sizing:border-box;margin:0;padding:0}
html,body{width:1200px;height:4367px;overflow:hidden}
body{position:relative;font-family:"Poppins",sans-serif;color:var(--ink);background:var(--white)}
.abs{position:absolute}
.serif{font-family:"Lora",serif}
.red{color:var(--red)}
.btn{display:inline-flex;align-items:center;justify-content:center;gap:6px;font-weight:500;font-size:13px;border-radius:3px}
.btn-red{background:var(--red);color:#fff}
.ph{display:block}

/* nav */
.nav{top:0;left:0;width:1200px;height:71px;background:#fff;display:flex;align-items:center}
.brand{position:absolute;left:78px;top:20px;font-weight:600;font-size:24px;color:var(--red)}
.nav-links{position:absolute;left:432px;top:26px;display:flex;gap:22px;font-size:14px;font-weight:500}
.nav-cta{position:absolute;left:985px;top:17px;width:139px;height:37px;border:1.5px solid var(--red);border-radius:20px;color:var(--red);font-size:11px;font-weight:500;display:flex;align-items:center;justify-content:center}

/* hero */
.hero{top:71px;left:0;width:1200px;height:556px;background:linear-gradient(180deg,#4d6278 0%,#9aa7a6 35%,#6f7b55 60%,#3c4430 100%)}
.hero-arc{top:560px;left:0;width:1200px;height:90px}
.hero h1{position:absolute;left:113px;top:118px;font-size:53px;font-weight:600;color:#fff}
.hero h2{position:absolute;left:113px;top:182px;font-size:40px;font-weight:500;color:#fff}
.hero p{position:absolute;left:113px;top:248px;font-size:16px;line-height:26px;color:#fff;width:340px}
.hero .b1{position:absolute;left:113px;top:367px;width:193px;height:47px;font-size:14px}
.hero .b2{position:absolute;left:316px;top:367px;width:192px;height:47px;background:#fff;color:var(--red);font-size:14px}

/* booking */
.book{top:586px;left:113px;width:973px;height:233px;background:var(--cream);box-shadow:0 6px 20px rgba(0,0,0,.12)}
.book .img{left:0;top:0;width:350px;height:233px;background:linear-gradient(180deg,#5e8fc6,#b7cde0 50%,#6d7a5b 70%,#3c3c3c)}
.book .welcome{left:381px;top:24px;font-size:14px}
.book .ttl{left:381px;top:48px;font-size:19px;font-weight:600}
.book .txt{left:381px;top:80px;width:330px;font-size:9px;line-height:15px;color:var(--grey)}
.book .contact{left:738px;top:24px;font-size:10px;color:var(--grey);line-height:14px}
.book .contact div{display:flex;gap:8px;align-items:flex-start;margin-bottom:14px}
.book .fields{left:380px;top:168px;width:520px;display:flex;border-top:1px solid #eadcb7;padding-top:0}
.field{display:flex;gap:10px;align-items:flex-start;font-size:12px;color:var(--grey);width:160px}
.field b{display:block;color:var(--red);font-weight:500;font-size:14px}
.book .search{left:834px;top:173px;width:110px;height:34px;font-size:12px}

/* section titles */
.sec-title{font-family:"Lora",serif;font-weight:500;font-size:38px;white-space:nowrap}
.sec-title::after{content:"";display:inline-block;width:42px;height:2px;background:var(--red);margin-left:4px;vertical-align:2px}
.sub{font-size:13px;color:var(--grey);line-height:20px;text-align:center}

/* destinations */
.card{width:437px;height:397px;background:#fff;box-shadow:0 4px 14px rgba(0,0,0,.1)}
.card .img{height:214px}
.card h4{position:absolute;left:18px;top:226px;font-size:15px;font-weight:600}
.card .tag{position:absolute;right:18px;top:228px;font-size:11px;color:var(--red)}
.card p{position:absolute;left:18px;top:254px;width:400px;font-size:10.5px;line-height:18px;color:var(--grey)}
.card .price{position:absolute;left:18px;top:300px;font-size:22px;font-weight:600;color:var(--red)}
.card .price span{color:var(--ink);font-size:17px;font-weight:500}
.card .stars{position:absolute;left:18px;top:352px;font-size:11px;color:var(--grey);display:flex;align-items:center;gap:6px}
.card .more{position:absolute;right:20px;top:345px;width:126px;height:32px;font-size:11px}
.arrowbtn{width:26px;height:26px;display:flex;align-items:center;justify-content:center;border-radius:2px}
.dots{top:1403px;left:572px;display:flex;gap:5px;align-items:center}
.dots i{width:6px;height:6px;border-radius:50%;background:#ccc}
.dots i.on{width:10px;height:10px;background:var(--red);box-shadow:0 0 0 2px #f6c9cb}

/* why */
.why{top:1490px;left:0;width:1200px;height:581px;background:var(--blush)}
.feature{left:617px;width:380px;display:flex;gap:18px}
.feature .ic{flex:none;width:54px;height:54px;border-radius:50%;display:flex;align-items:center;justify-content:center}
.feature h5{font-size:19px;font-weight:500;margin-bottom:4px}
.feature p{font-size:11px;line-height:18px;color:var(--grey)}

/* fleet */
.tile{border-radius:6px;overflow:hidden}
.tile span{position:absolute;left:0;right:0;bottom:0;height:42px;background:linear-gradient(0deg,rgba(0,0,0,.5),transparent);color:#fff;font-weight:600;font-size:15px;display:flex;align-items:flex-end;justify-content:center;padding-bottom:8px}

/* testimonials */
.testi{top:2936px;left:0;width:1200px;height:467px;background:linear-gradient(180deg,#c21d25,#b41c22)}
.tcard{top:3136px;width:289px;height:168px;background:#fbe9ea;border-radius:8px;padding:18px 20px}
.tcard .who{display:flex;align-items:center;gap:10px;font-size:12px}
.tcard .av{width:32px;height:32px;border-radius:50%;background:#d9b08c}
.tcard .st{color:#e2a12a;font-size:9px;letter-spacing:1px}
.tcard .q{position:absolute;right:22px;top:14px;color:var(--red);font-family:"Lora",serif;font-size:36px;line-height:1}
.tcard p{margin-top:14px;font-size:10.5px;line-height:18px;color:#444}

/* contact */
.input{border:1.5px solid #bbb;border-radius:4px;font-size:12px;color:var(--grey);padding:0 14px;display:flex;align-items:center}

/* footer */
.footer{top:4009px;left:0;width:1200px;height:358px;background:var(--footer);color:#fff}
.footer h6{font-size:15px;font-weight:500;margin-bottom:22px}
.footer li{list-style:none;font-size:12px;color:#ddd;margin-bottom:20px}
</style>
</head>
<body>

<!-- navigation -->
<header class="abs nav">
  <div class="brand">Lenz Tavan</div>
  <nav class="nav-links"><span>Unsere Reisen</span><span>Busvermietung</span><span>Speisekarte ⌄</span></nav>
  <div class="nav-cta">Buchen Sie jetzt</div>
</header>

<!-- hero -->
<section class="abs hero" role="img" aria-label="Video-Header: Reisebus auf einer Landstrasse bei Sonnenuntergang">
  <h1 class="serif">Entdecken Sie Europa</h1>
  <h2 class="serif">Mit Komfort Und Stil</h2>
  <p>Über 40 Jahre Zuverlässige Busreisen &amp; Vermietung In Graubünden</p>
  <span class="btn btn-red b1">Entdecken Sie Touren</span>
  <span class="btn b2">Buchen Sie einen Bus</span>
</section>
<svg class="abs hero-arc" viewBox="0 0 1200 90" preserveAspectRatio="none"><path d="M0 40 Q600 -30 1200 40 L1200 90 L0 90Z" fill="#fff"/><path d="M0 40 Q600 -30 1200 40 L1200 55 Q600 -12 0 62Z" fill="var(--red)"/></svg>

<!-- booking card -->
<section class="abs book">
  <div class="abs img" role="img" aria-label="Weisser Reisebus auf der Autobahn unter blauem Himmel"></div>
  <div class="abs welcome">Willkommen!</div>
  <div class="abs ttl">Buchen Sie Ihre Reise <span class="red">Mit Lenz Tavan</span></div>
  <div class="abs txt">Lorem ipsum ist einfach Blindtext der Druck- und Satzindustrie. Lorem ipsum ist seit dem 16. Jahrhundert der Standardblindtext der Industrie. Einfach Blindtext der Druck- und Satzindustrie.</div>
  <div class="abs contact">
    <div><svg width="14" height="16" viewBox="0 0 14 16"><path d="M7 15s5-5 5-9A5 5 0 0 0 2 6c0 4 5 9 5 9z" fill="none" stroke="#c8191f" stroke-width="1.4"/><circle cx="7" cy="6" r="2" fill="none" stroke="#c8191f" stroke-width="1.4"/></svg><span>C/O Marco Beispiel Car-Reisen AG<br>Talstrasse 8 CH-7000 Musterdorf</span></div>
    <div><svg width="14" height="14" viewBox="0 0 14 14"><path d="M2 1h3l1 3-2 1a8 8 0 0 0 4 4l1-2 3 1v3c0 1-1 1-2 1A11 11 0 0 1 1 3c0-1 0-2 1-2z" fill="none" stroke="#c8191f" stroke-width="1.3"/></svg><span>+41(0)81 000 12 34</span></div>
    <div><svg width="14" height="12" viewBox="0 0 14 12"><rect x="1" y="1" width="12" height="10" fill="none" stroke="#c8191f" stroke-width="1.3"/><path d="M1 1l6 5 6-5" fill="none" stroke="#c8191f" stroke-width="1.3"/></svg><span>info(at)lenztavan-beispiel.ch</span></div>
  </div>
  <div class="abs fields" style="border:none">
    <div class="field"><svg width="18" height="18" viewBox="0 0 18 18"><rect x="2" y="3" width="14" height="13" fill="none" stroke="#777" stroke-width="1.3"/><path d="M2 7h14M6 1v4M12 1v4" stroke="#777" stroke-width="1.3"/></svg><div><b>Datum</b>Datum</div></div>
    <div class="field"><svg width="18" height="18" viewBox="0 0 18 18"><circle cx="7" cy="6" r="3" fill="none" stroke="#777" stroke-width="1.3"/><path d="M7 16s5-4 5-8" fill="none" stroke="#777" stroke-width="1.3"/></svg><div><b>Standort</b>Standort</div></div>
    <div class="field"><svg width="18" height="18" viewBox="0 0 18 18"><circle cx="9" cy="6" r="3.5" fill="none" stroke="#777" stroke-width="1.3"/><path d="M2 17c1-4 4-6 7-6s6 2 7 6" fill="none" stroke="#777" stroke-width="1.3"/></svg><div><b>Mitglied</b>Mitglied</div></div>
  </div>
  <span class="abs btn btn-red search"><svg width="12" height="12" viewBox="0 0 12 12"><circle cx="5" cy="5" r="3.8" fill="none" stroke="#fff" stroke-width="1.4"/><path d="M8 8l3 3" stroke="#fff" stroke-width="1.4"/></svg>Search Trip</span>
</section>

<!-- destinations -->
<h2 class="abs sec-title" style="left:141px;top:905px">Beliebte <span class="red">Reiseziele</span></h2>
<div class="abs arrowbtn" style="left:93px;top:1155px;border:1px solid #ccc"><svg width="12" height="10" viewBox="0 0 12 10"><path d="M11 5H1M5 1L1 5l4 4" fill="none" stroke="#333" stroke-width="1.4"/></svg></div>
<div class="abs arrowbtn" style="left:1081px;top:1155px;background:var(--red)"><svg width="12" height="10" viewBox="0 0 12 10"><path d="M1 5h10M7 1l4 4-4 4" fill="none" stroke="#fff" stroke-width="1.4"/></svg></div>

<article class="abs card" style="left:141px;top:968px">
  <div class="img" role="img" aria-label="Bunte Häuserfront am Comer See mit Booten" style="background:linear-gradient(180deg,#6aa7dc,#e0a15a 45%,#b86842 65%,#3d6f8a)"></div>
  <h4>Einkaufstour Nach Como</h4><span class="tag">● 1-Tages-Tour</span>
  <p>Lorem Ipsum Ist Einfach Ein Blindtext Der Druck- Und Satzindustrie. Lorem Ipsum Ist Seit</p>
  <div class="price">50.000/<span>Pro Person</span></div>
  <div class="stars"><span style="color:#e2a12a;font-size:15px;letter-spacing:3px">★★★★★</span>4,9 Bewertungen</div>
  <span class="btn btn-red more">Learn More →</span>
</article>
<article class="abs card" style="left:622px;top:968px">
  <div class="img" role="img" aria-label="Innsbruck mit Herbstbäumen und Bergkulisse" style="background:linear-gradient(180deg,#3b79c4,#a4b3c4 40%,#c58b3b 65%,#6f5a3d)"></div>
  <h4>Innsbruck</h4><span class="tag">● 3-Tägige Tour</span>
  <p>Lorem Ipsum Ist Einfach Ein Blindtext Der Druck- Und Satzindustrie. Lorem Ipsum Ist Seit</p>
  <div class="price">42.000/<span>Pro Person</span></div>
  <div class="stars"><span style="color:#e2a12a;font-size:15px;letter-spacing:3px">★★★★★</span>4,9 Bewertungen</div>
  <span class="btn btn-red more">Learn More →</span>
</article>
<div class="abs dots"><i></i><i></i><i class="on"></i><i></i><i></i></div>

<!-- why us -->
<section class="abs why"></section>
<div class="abs" style="left:134px;top:1660px;width:357px;height:280px;background:#eab8bb"></div>
<div class="abs" role="img" aria-label="Reisebus auf einer Landstrasse im Gegenlicht" style="left:149px;top:1620px;width:380px;height:305px;background:linear-gradient(180deg,#5b88c0,#dfe6e8 40%,#7f8c6a 70%,#3d4a2d)"></div>
<h2 class="abs sec-title" style="left:617px;top:1585px">Warum mit uns <span class="red">reisen?</span></h2>
<div class="abs" style="left:617px;top:1636px;font-size:13px;color:var(--grey)">Reisen Sie Mit Vertrauen Und Komfort.</div>
<div class="abs feature" style="top:1685px"><div class="ic" style="background:var(--red)"><svg width="26" height="20" viewBox="0 0 26 20"><rect x="2" y="3" width="22" height="12" rx="3" fill="none" stroke="#fff" stroke-width="1.6"/><path d="M2 9h22" stroke="#fff" stroke-width="1.4"/><circle cx="7" cy="16" r="2" fill="#fff"/><circle cx="19" cy="16" r="2" fill="#fff"/></svg></div><div><h5>Über 40 Jahre <span class="red">Erfahrung</span></h5><p>Lorem Ipsum Ist Einfach Ein Blindtext Der Druck- Und Satzindustrie. Lorem Ipsum War Der Star Der Branche Lorem Ipsum Ist Einfach Dumm</p></div></div>
<div class="abs feature" style="top:1788px"><div class="ic" style="background:#3a3a3a"><svg width="24" height="24" viewBox="0 0 24 24"><rect x="5" y="3" width="14" height="16" rx="3" fill="none" stroke="#fff" stroke-width="1.6"/><path d="M5 11h14" stroke="#fff" stroke-width="1.4"/><circle cx="9" cy="15" r="1.3" fill="#fff"/><circle cx="15" cy="15" r="1.3" fill="#fff"/></svg></div><div><h5>Luxus<span class="red">busse</span></h5><p>Lorem Ipsum Ist Einfach Ein Blindtext Der Druck- Und Satzindustrie. Lorem Ipsum War Der Star Der Branche Lorem Ipsum Ist Einfach Dumm</p></div></div>
<div class="abs feature" style="top:1891px"><div class="ic" style="background:var(--red)"><svg width="24" height="24" viewBox="0 0 24 24"><circle cx="12" cy="8" r="4" fill="none" stroke="#fff" stroke-width="1.6"/><path d="M4 21c1-5 4-7 8-7s7 2 8 7" fill="none" stroke="#fff" stroke-width="1.6"/></svg></div><div><h5>Experten<span class="red">führer</span></h5><p>Lorem Ipsum Ist Einfach Ein Blindtext Der Druck- Und Satzindustrie. Lorem Ipsum War Der Star Der Branche Lorem Ipsum Ist Einfach Dumm</p></div></div>

<!-- fleet -->
<h2 class="abs sec-title" style="left:362px;top:2137px">Unsere moderne <span class="red">Flotte</span></h2>
<p class="abs sub" style="left:290px;top:2196px;width:620px">Lorem Ipsum ist einfach ein Blindtext der Druck- und Satzindustrie. Lorem Ipsum war der Star der Branche&nbsp; Lorem Ipsum ist einfach dumm</p>
<div class="abs tile" role="img" aria-label="Innenraum mit Tisch und Sitzbereich" style="left:141px;top:2248px;width:290px;height:307px;background:linear-gradient(180deg,#e6e2dc,#b8b1a8 60%,#5b5a58)"><span>Bequemes Sitzen</span></div>
<div class="abs tile" role="img" aria-label="Deckenpanel mit Klimaanlage" style="left:455px;top:2248px;width:290px;height:194px;background:linear-gradient(180deg,#cfcfd1,#8f8e94 50%,#6f3a45)"><span>Klimaanlage</span></div>
<div class="abs tile" role="img" aria-label="Blaue Polstersitze im Reisebus" style="left:769px;top:2248px;width:290px;height:194px;background:linear-gradient(180deg,#b7b8bb,#4b5680 55%,#2a3054)"><span>Bequemes Sitzen</span></div>
<div class="abs tile" role="img" aria-label="Bordtoilette im Reisebus" style="left:141px;top:2580px;width:290px;height:201px;background:linear-gradient(90deg,#d8dae6,#f1f1f3 50%,#8b8a8f)"><span>Bord-WC</span></div>
<div class="abs tile" role="img" aria-label="Reihen hellbrauner Ledersitze im Reisebus" style="left:458px;top:2467px;width:601px;height:314px;background:linear-gradient(180deg,#8fb3c6,#c9a277 45%,#9a6b3d)"><span>Bequemes Sitzen</span></div>
<span class="abs btn btn-red" style="left:519px;top:2817px;width:162px;height:41px">View More →</span>

<!-- testimonials -->
<section class="abs testi" role="img" aria-label="Hintergrund: Küstenstrasse in rotem Farbton"></section>
<h2 class="abs sec-title" style="left:302px;top:2992px;color:#fff">Was soll unser Kunde sagen?</h2>
<p class="abs sub" style="left:330px;top:3052px;width:540px;color:#f6d6d8">Lorem ipsum ist einfach ein Blindtext der Druck- und Satzindustrie. Lorem ipsum war der Star der Branche Lorem Ipsum ist einfach dumm</p>
<div class="abs tcard" style="left:141px"><div class="who"><i class="av"></i><div>Lena Brunner<div class="st">★★★★★</div></div></div><span class="q">“</span><p>Lorem ipsum dolor sit amet consectetur. Porttitor mi ac justo ultrices tortor ipsum nec eget est. Velit hendrerit vel tristique gravida euismod lacus luctus. vel tristique gravida euismod</p></div>
<div class="abs tcard" style="left:455px"><div class="who"><i class="av" style="background:#c9a48a"></i><div>Peter Caduff<div class="st">★★★★★</div></div></div><span class="q">“</span><p>Lorem ipsum dolor sit amet consectetur. Porttitor mi ac justo ultrices tortor ipsum nec eget est. Velit hendrerit vel tristique gravida euismod lacus luctus. vel tristique gravida euismod</p></div>
<div class="abs tcard" style="left:770px"><div class="who"><i class="av" style="background:#8a7a70"></i><div>Anna Meier<div class="st">★★★★★</div></div></div><span class="q">“</span><p>Lorem ipsum dolor sit amet consectetur. Porttitor mi ac justo ultrices tortor ipsum nec eget est. Velit hendrerit vel tristique gravida euismod lacus luctus. vel tristique gravida euismod</p></div>
<div class="abs" style="left:544px;top:3324px;display:flex;gap:8px"><i style="width:28px;height:2px;background:#e99"></i><i style="width:42px;height:3px;background:#fff"></i><i style="width:28px;height:2px;background:#e99"></i></div>

<!-- contact -->
<h2 class="abs sec-title" style="left:378px;top:3468px">Kontaktieren <span class="red">Sie uns</span></h2>
<p class="abs sub" style="left:290px;top:3527px;width:620px">Lorem Ipsum ist einfach ein Blindtext der Druck- und Satzindustrie. Lorem Ipsum war der Star der Branche&nbsp; Lorem Ipsum ist einfach dumm</p>
<div class="abs" style="left:141px;top:3628px;width:412px;height:291px;background:#f2c7c9"></div>
<div class="abs" role="img" aria-label="Lächelnder Fahrgast im Reisebus" style="left:163px;top:3593px;width:420px;height:302px;background:linear-gradient(120deg,#d08a4a,#6b4b3a 45%,#2f2a30)"></div>
<div class="abs input" style="left:626px;top:3593px;width:208px;height:47px">Vorname</div>
<div class="abs input" style="left:851px;top:3593px;width:208px;height:47px">Nachname</div>
<div class="abs input" style="left:626px;top:3655px;width:433px;height:47px">E-Mail</div>
<div class="abs input" style="left:626px;top:3717px;width:433px;height:138px;align-items:flex-start;padding-top:16px">Ihre Nachricht</div>
<span class="abs btn btn-red" style="left:911px;top:3880px;width:148px;height:51px;font-size:15px">Schicken</span>

<!-- footer -->
<footer class="abs footer">
  <div class="abs" style="left:92px;top:72px;font-size:28px;font-weight:600;color:var(--red)">Lenz Tavan</div>
  <p class="abs" style="left:92px;top:134px;width:210px;font-size:11px;line-height:19px;color:#ddd">Lorem ipsum ist einfach ein Blindtext der Druck- und Satzindustrie. Lorem ipsum war der Star der Branche</p>
  <div class="abs" style="left:380px;top:78px"><h6>Schnelllink</h6><ul><li>Unsere Reisen</li><li>Busvermietung</li><li>Speisekarte</li><li>Über uns</li></ul></div>
  <div class="abs" style="left:556px;top:78px"><h6>Reisen Sie mit uns?</h6><ul><li>Über 40 Jahre Erfahrung</li><li>Luxusbusse</li><li>Expertenführer</li></ul></div>
  <div class="abs" style="left:799px;top:78px;width:330px;font-size:12px;color:#ddd;line-height:17px"><h6 style="color:#fff">Kontaktieren Sie uns</h6>
    <div style="display:flex;gap:10px;margin-bottom:18px"><span class="red">⚲</span>c/o Marco Beispiel Car-Reisen AG Talstrasse 8 CH-7000 Musterdorf</div>
    <div style="display:flex;gap:10px;margin-bottom:18px"><span class="red">✆</span>+41(0)81 000 12 34</div>
    <div style="display:flex;gap:10px"><span class="red">✉</span>info(at)lenztavan-beispiel.ch</div>
  </div>
  <div class="abs" style="left:0;top:329px;width:1200px;text-align:center;font-size:11px;color:#ccc">Lenz Tavan © 2025 Alle Rechte vorbehalten</div>
</footer>

</body>
</html>
```